Plinkora Advertisement for EV chargers

Project Overview:
We are excited to launch a new Plinkora ad campaign to promote our top-notch service of Electric Vehicle (EV) Charger Installation. This campaign aims to reach environmentally conscious individuals, homeowners, businesses, and EV owners seeking professional and reliable EV charger installation solutions. The primary goal is to increase brand awareness and generate leads for our EV charger installation service.
Target Audience:
Our target audience includes environmentally conscious homeowners, property managers, commercial businesses, and individuals who own or plan to purchase an electric vehicle. The age range for our target audience is between 25 to 65 years old, residing in [your service area location] or nearby regions.
Key Message:
The advertisement should convey the following key messages:
"Power Up Your Ride with Professional EV Charger Installation."
"Fast and Reliable Service for Home and Business EV Charging Solutions."
"Go Green with Clean Energy and Eco-friendly EV Charging."
"Experienced Installers for Hassle-free EV Charger Setups."
Design Requirements:
Dimensions: The advertisement should comply with Plinkora's recommended ad dimensions (e.g., 1200 x 628 pixels).
Branding: Incorporate our company logo and colors (Logo attached).
Visuals: Use high-quality images or graphics showcasing electric vehicles being charged at home and in commercial settings, highlighting the ease and convenience of the process.
Call-to-Action (CTA): Include a clear and compelling CTA button, such as "Get a Quote," "Book Now," or "Learn More."
Text: Keep the text concise, using persuasive language to emphasize the benefits of our EV charger installation service, such as expert technicians, efficient installations, and cost savings.
Testimonials: Feature positive customer reviews or testimonials (if available) to build trust and credibility.
Coverage Area: Mention your service coverage area to ensure relevancy to the target audience.
Offer: If applicable, consider offering a limited-time discount or promotion for EV charger installation services.
Target Market(s)
Target Audience: Our target audience includes environmentally conscious homeowners, property managers, commercial businesses, and individuals who own or plan to purchase an electric vehicle. The age range for our target audience is between 25 to 65 years old, residing in [your service area location] or nearby regions.
Requirements
Must have
- The advertisement should convey the following key messages: "Power Up Your Ride with Professional EV Charger Installation." "Fast and Reliable Service for Home and Business EV Charging Solutions." "Go Green with Clean Energy and Eco-friendly EV Charging." "Experienced Installers for Hassle-free EV Charger Setups." Design Requirements: Dimensions: The advertisement should comply with Plinkora's recommended ad dimensions (e.g., 1200 x 628 pixels). Branding: Incorporate our company logo and colors (Logo attached). Visuals: Use high-quality images or graphics showcasing electric vehicles being charged at home and in commercial settings, highlighting the ease and convenience of the process. Call-to-Action (CTA): Include a clear and compelling CTA button, such as "Get a Quote," "Book Now," or "Learn More." Text: Keep the text concise, using persuasive language to emphasize the benefits of our EV charger installation service, such as expert technicians, efficient installations, and cost savings. Testimonials: Feature positive customer reviews or testimonials (if available) to build trust and credibility. Coverage Area: Mention your service coverage area to ensure relevancy to the target audience. Offer: If applicable, consider offering a limited-time discount or promotion for EV charger installation services.

```html
<!DOCTYPE html>
<html lang="en">
<head>
<meta charset="utf-8">
<title>Voltmere Energy – EV Charging Solutions</title>
<link rel="stylesheet" href="https://fonts.googleapis.com/css2?family=Poppins:ital,wght@0,300;0,600;0,700;1,400&display=swap">
<style>
  :root {
    --brand-red: #b5172e;
    --home-tint-top: #c7303f;
    --home-tint-bottom: #a8293a;
    --business-tint-top: #4a5259;
    --business-tint-bottom: #2f363c;
    --white: #ffffff;
    --ink: #1d1d1f;
  }
  * { margin: 0; padding: 0; box-sizing: border-box; }
  html, body { width: 1200px; height: 628px; overflow: hidden; background: #ffffff; }
  .ad {
    position: relative;
    width: 1200px;
    height: 628px;
    overflow: hidden;
    font-family: "Poppins", sans-serif;
    color: var(--white);
  }
  .scene {
    position: absolute;
    top: 0;
    height: 628px;
    width: 600px;
  }
  .scene--home {
    left: 0;
    background:
      radial-gradient(ellipse at 45% 60%, rgba(255,255,255,0.12), transparent 60%),
      linear-gradient(180deg, var(--home-tint-top), var(--home-tint-bottom));
  }
  .scene--business {
    left: 600px;
    background:
      radial-gradient(ellipse at 40% 45%, rgba(255,255,255,0.10), transparent 60%),
      linear-gradient(180deg, var(--business-tint-top), var(--business-tint-bottom));
  }
  .brand {
    position: absolute;
    top: 44px;
    right: 48px;
    display: flex;
    flex-direction: column;
    align-items: flex-end;
  }
  .brand__name {
    font-weight: 600;
    font-size: 20px;
    line-height: 1.1;
    color: var(--brand-red);
    letter-spacing: 0.3px;
  }
  .brand__tagline {
    margin-top: 6px;
    font-weight: 600;
    font-size: 7.5px;
    letter-spacing: 0.2px;
    color: var(--ink);
  }
  .headline-group {
    position: absolute;
    left: 0;
    right: 0;
    top: 180px;
    text-align: center;
  }
  .kicker {
    font-weight: 300;
    font-size: 33px;
    line-height: 48px;
    letter-spacing: 0.2px;
  }
  .headline {
    margin-top: 6px;
    font-weight: 700;
    font-size: 71px;
    line-height: 74px;
    letter-spacing: 0.5px;
  }
  .intro {
    position: absolute;
    top: 352px;
    left: 345px;
    width: 510px;
    text-align: center;
    font-style: italic;
    font-weight: 400;
    font-size: 16.5px;
    line-height: 1.45;
  }
  .cta {
    position: absolute;
    left: 447px;
    top: 500px;
    width: 306px;
    height: 54px;
    border-radius: 8px;
    background: var(--brand-red);
    color: var(--white);
    font-weight: 600;
    font-size: 27px;
    display: flex;
    align-items: center;
    justify-content: center;
    letter-spacing: 0.3px;
    box-shadow: 0 4px 10px rgba(0,0,0,0.2);
  }
</style>
</head>
<body>
  <main class="ad">
    <div class="scene scene--home" role="img" aria-label="Photo of a woman standing beside a white electric car charging from a wall-mounted home charger, tinted red"></div>
    <div class="scene scene--business" role="img" aria-label="Photo of a smiling man plugging a charging cable into an electric car at a commercial charging station, tinted dark grey"></div>

    <div class="brand">
      <span class="brand__name">VOLTMERE ENERGY</span>
      <span class="brand__tagline">ELECTRICAL INSTALLATION AND SUPPORT</span>
    </div>

    <header class="headline-group">
      <p class="kicker">Fast and Reliable Service for Home and Business</p>
      <h1 class="headline">EV CHARGING SOLUTIONS</h1>
    </header>

    <p class="intro">We understand that every business or home has different energy requirements. This is why we implement a collaborative approach and customise a package to align with your energy goals.</p>

    <div class="cta">GET A QUOTE</div>
  </main>
</body>
</html>
```